Website for an AdOps/Media Agency

We need a logo for an ad operations firm. We help websites to maximize their advertising revenues by optimizing their ad networks, configurations, technologies, etc. The name is Zornival, or ZorNival, to communicate that we take them to the top of their revenue potential. We want to also communicate, trust us to handle your adops, we take care of the hassle (it's an industry in continual technological innovation -- hard to stay on top of, and heavily manual, reporting, etc) and make sure our clients maximize ad revenues. For more info on site ideas/desires: https://files.brelmora.com/doc/7QxTbn2Lw9Rk4Vz8Hc3Md6Fp1Ys5Ga0Je/view?usp=sharing
Updates

Project Deadline Extended Reason: Apologies, I got caught up in other things. This is now priority, and will be guaranteed. I will also include an extra coding fee for a WP site and increase the budget. Thanks for your understanding! Added Thursday, July 7, 2016

Target Market(s)

Ad Operations/Media Consultancy

Industry/Entity Type

Ad Agency

Number of Pages Required

1 page

Font styles to use
Sans Serif

Requirements
Must have
• I like clean and simple, nice images, scrolling down.
Nice to have
• I like clean, fresh white running through the site. Note, I listed us as an ad agency, but only because there was no adops. We work with ad agencies, but we are more agents for publishers.
Should not have
• To much clutter.

```html
<!DOCTYPE html>
<html lang="en">
<head>
<meta charset="utf-8">
<title>Zornival — Ad Operations</title>
<link rel="stylesheet" href="https://fonts.googleapis.com/css2?family=Poppins:wght@400;500;600&family=Lato:ital,wght@0,400;0,700;1,400&display=swap">
<style>
:root{
  --green:#2e9e2a;
  --green-dark:#27861f;
  --ink:#222;
  --text:#444;
  --topbar:#3b3b3b;
  --footer:#2b2b2b;
  --footer-line:#3d3d3d;
  --light:#ececec;
  --white:#fff;
  --icon:#555;
}
*{box-sizing:border-box;margin:0;padding:0}
html,body{width:1200px;height:2410px;overflow:hidden}
body{position:relative;font-family:"Lato",sans-serif;color:var(--text);background:var(--white)}
.abs{position:absolute}

/* top bar */
.topbar{position:absolute;left:0;top:0;width:1200px;height:29px;background:var(--topbar);color:var(--white);font-size:13px}
.topbar .contact{position:absolute;right:52px;top:6px;display:flex;gap:22px;align-items:center}
.topbar .contact span{display:flex;align-items:center;gap:7px}

/* header */
.site-header{position:absolute;left:0;top:29px;width:1200px;height:89px;background:var(--white)}
.brand{position:absolute;left:132px;top:13px;display:flex;align-items:center;gap:22px;height:64px}
.brand-square{width:62px;height:62px;border:4px solid var(--ink);border-radius:8px}
.brand-name{font-family:"Poppins",sans-serif;font-weight:500;font-size:44px;color:var(--green);letter-spacing:-.5px}
.main-nav{position:absolute;top:32px;left:0;font-family:"Poppins",sans-serif;font-size:16px;color:var(--ink)}
.main-nav a{position:absolute;white-space:nowrap;color:inherit;text-decoration:none}
.main-nav .active{background:var(--green);color:var(--white);font-weight:600;padding:4px 12px;top:-4px;border-radius:2px}
.main-nav .sep{position:absolute;top:4px;width:1px;height:14px;background:#bbb}

/* hero */
.hero{position:absolute;left:0;top:118px;width:1200px;height:481px;background:linear-gradient(180deg,#9fb3c8 0%,#c9d6e3 45%,#eef2f6 75%,#dfe6ee 100%)}
.hero-copy{position:absolute;right:137px;top:96px;text-align:right;color:#111;font-family:"Poppins",sans-serif}
.hero-copy h1{font-size:41px;font-weight:600;line-height:52px}
.hero-copy p{font-size:29px;line-height:42px;margin-top:10px}
.slider-arrow{position:absolute;top:253px;width:32px;height:32px}

/* welcome */
.welcome{position:absolute;left:0;top:599px;width:1200px;height:379px;text-align:center}
.welcome-mark{position:absolute;left:577px;top:32px;width:60px;height:60px;border:4px solid var(--ink);border-radius:6px}
.section-title{font-family:"Poppins",sans-serif;font-weight:500;font-size:31px;color:var(--ink)}
.rule{width:56px;height:4px;background:var(--green);margin:12px auto 0}
.welcome .section-title{position:absolute;left:0;right:0;top:108px}
.welcome .rule{position:absolute;left:572px;top:154px;margin:0}
.welcome p{position:absolute;left:137px;width:926px;top:186px;font-size:14px;line-height:25px;color:#333}
.btn-dark{position:absolute;left:535px;top:299px;width:130px;height:38px;background:#1f2a26;color:var(--white);font-weight:700;font-size:14px;line-height:38px;text-align:center}

/* services */
.services{position:absolute;left:0;top:978px;width:1200px;height:768px;background:var(--green);color:var(--white)}
.services .section-title{position:absolute;left:0;right:0;top:30px;text-align:center;color:var(--white)}
.services .rule{position:absolute;left:572px;top:82px;margin:0;background:var(--white)}
.service{position:absolute;width:220px;margin-left:-110px;text-align:center}
.service-icon{width:96px;height:96px;margin:0 auto;background:var(--white);border:4px solid #1d1d1d;border-radius:8px;display:flex;align-items:center;justify-content:center}
.service-icon svg{width:60px;height:60px}
.service h3{margin-top:17px;font-family:"Poppins",sans-serif;font-weight:500;font-size:16.5px;line-height:21px;letter-spacing:.2px}

/* testimonials */
.testimonials{position:absolute;left:0;top:1746px;width:1200px;height:318px;background:var(--light)}
.testimonials .section-title{position:absolute;left:0;right:0;top:38px;text-align:center;font-weight:600}
.testimonials .rule{position:absolute;left:572px;top:88px;margin:0;background:var(--ink)}
.avatar{position:absolute;left:153px;top:132px;width:118px;height:118px;border-radius:50%;border:4px solid var(--white);background:radial-gradient(circle at 50% 40%,#e2c3a8 0%,#c9a487 45%,#a9b8c6 100%);box-shadow:0 0 0 1px #ccc}
.quote-mark{position:absolute;left:281px;top:133px;font-family:"Poppins",sans-serif;font-size:60px;color:#c9c9c9;line-height:1}
.quote{position:absolute;left:289px;top:142px;width:770px;font-style:italic;font-size:13px;line-height:24px;color:#333}
.quote-author{position:absolute;left:292px;top:247px;font-style:italic;font-size:13px;color:#333}
.more-link{position:absolute;left:917px;top:247px;font-size:13px;color:#333;text-decoration:underline}

/* footer */
.site-footer{position:absolute;left:0;top:2064px;width:1200px;height:298px;background:var(--footer);color:var(--white)}
.footer-col{position:absolute;top:38px}
.footer-col h4{font-family:"Poppins",sans-serif;font-weight:500;font-size:18px;padding-bottom:8px;border-bottom:1px solid var(--footer-line)}
.quick-links{left:53px;width:108px}
.quick-links ul{list-style:none;margin-top:8px}
.quick-links li{font-size:13px;height:43px;line-height:26px;padding-left:10px;position:relative}
.quick-links li::before{content:"›";position:absolute;left:0}
.col-divider{position:absolute;top:38px;width:1px;height:240px;background:var(--footer-line)}
.contact-details{left:262px;width:196px;font-size:13px;line-height:21px}
.contact-details .line{display:flex;gap:10px;align-items:center;margin-top:26px}
.contact-details address{font-style:normal;margin-top:10px}
.inquiry{left:562px;width:296px}
.field{position:absolute;left:-3px;width:296px;background:var(--white);border-radius:2px;color:#555;font-size:12px;padding:6px 10px}
.btn-submit{position:absolute;left:-3px;top:223px;width:136px;height:35px;background:var(--green);color:var(--white);font-family:"Poppins",sans-serif;font-weight:600;font-size:17px;text-align:center;line-height:35px}
.footer-mark{position:absolute;left:964px;top:45px;width:181px;height:180px;border:8px solid #555;border-radius:18px}
.copyright{position:absolute;left:0;top:2362px;width:1200px;height:48px;background:var(--green);color:var(--white);text-align:center;font-family:"Poppins",sans-serif;font-size:15px;line-height:48px}
</style>
</head>
<body>

<div class="topbar">
  <div class="contact">
    <span><svg width="13" height="13" viewBox="0 0 24 24"><path fill="#fff" d="M6.6 10.8a15 15 0 0 0 6.6 6.6l2.2-2.2c.3-.3.7-.4 1-.2 1.1.4 2.3.6 3.6.6.6 0 1 .4 1 1V20c0 .6-.4 1-1 1A17 17 0 0 1 3 4c0-.6.4-1 1-1h3.5c.6 0 1 .4 1 1 0 1.3.2 2.5.6 3.6.1.3 0 .7-.2 1z"/></svg>555-014-2768</span>
    <span><svg width="14" height="11" viewBox="0 0 24 18"><path fill="#fff" d="M0 0h24v18H0z"/><path d="M0 0l12 9L24 0" stroke="#3b3b3b" stroke-width="2" fill="none"/></svg>info@zornival.com</span>
  </div>
</div>

<header class="site-header">
  <div class="brand">
    <div class="brand-square"></div>
    <div class="brand-name">zornival</div>
  </div>
  <nav class="main-nav">
    <a class="active" href="#" style="left:597px">Home</a>
    <span class="sep" style="left:681px"></span>
    <a href="#" style="left:706px">About Us</a>
    <span class="sep" style="left:794px"></span>
    <a href="#" style="left:818px">Publisher</a>
    <span class="sep" style="left:910px"></span>
    <a href="#" style="left:934px">Advertiser</a>
    <span class="sep" style="left:1031px"></span>
    <a href="#" style="left:1057px">Contact Us</a>
  </nav>
</header>

<section class="hero" role="img" aria-label="Photo of two climbers helping each other up a snowy mountain summit">
  <div class="hero-copy">
    <h1>Let Our Team Help<br>Your Team</h1>
    <p>We Can Help You Take Your<br>Revenues To The Next Level</p>
  </div>
  <svg class="slider-arrow" style="left:8px" viewBox="0 0 32 32"><circle cx="16" cy="16" r="15" fill="#333" stroke="#fff" stroke-width="2"/><path d="M19 9l-7 7 7 7" stroke="#fff" stroke-width="3" fill="none"/></svg>
  <svg class="slider-arrow" style="left:1160px" viewBox="0 0 32 32"><circle cx="16" cy="16" r="15" fill="#333" stroke="#fff" stroke-width="2"/><path d="M13 9l7 7-7 7" stroke="#fff" stroke-width="3" fill="none"/></svg>
</section>

<section class="welcome">
  <div class="welcome-mark"></div>
  <h2 class="section-title">Welcome To Zornival</h2>
  <div class="rule"></div>
  <p>Lorem ipsum dolor sit amet, consectetuer adipiscing elit, sed diam nonummy nibh euismod tincidunt ut laoreet dolore magna aliquam erat volutpat. Ut wisi enim ad minim veniam, quis nostrud exerci tation ullamcorper suscipit lobortis nisl ut aliquip ex ea commodo consequat. Duis autem vel eum iriure dolor in hendrerit in vulputate velit esse molestie consequat, vel illum dolore eu feugiat nulla facilisis at vero eros et accumsan et iusto odio dignissim qui blandit praesent luptatum zzril delenit augue duis dolore te feugait nulla facilisi.</p>
  <a class="btn-dark">Read More</a>
</section>

<section class="services">
  <h2 class="section-title">Our Services</h2>
  <div class="rule"></div>

  <div class="service" style="left:194px;top:124px">
    <div class="service-icon"><svg viewBox="0 0 60 60"><g fill="var(--icon)"><rect x="8" y="40" width="8" height="14"/><rect x="20" y="34" width="8" height="20"/><rect x="32" y="28" width="8" height="26"/><rect x="44" y="22" width="8" height="32"/></g><path d="M6 34L22 20l10 8 18-18" stroke="var(--icon)" stroke-width="4" fill="none"/><path d="M42 8h10v10z" fill="var(--icon)"/></svg></div>
    <h3>Monetization<br>Strategy &amp; Planning</h3>
  </div>
  <div class="service" style="left:382px;top:124px">
    <div class="service-icon"><svg viewBox="0 0 60 60"><g stroke="var(--icon)" stroke-width="3"><line x1="30" y1="30" x2="30" y2="8"/><line x1="30" y1="30" x2="30" y2="52"/><line x1="30" y1="30" x2="8" y2="30"/><line x1="30" y1="30" x2="52" y2="30"/><line x1="30" y1="30" x2="14" y2="14"/><line x1="30" y1="30" x2="46" y2="46"/></g><g fill="var(--icon)"><circle cx="30" cy="30" r="11"/><circle cx="30" cy="7" r="5"/><circle cx="30" cy="53" r="5"/><circle cx="7" cy="30" r="5"/><circle cx="53" cy="30" r="5"/><circle cx="13" cy="13" r="5"/><circle cx="47" cy="47" r="5"/></g></svg></div>
    <h3>Network<br>Configurations</h3>
  </div>
  <div class="service" style="left:573px;top:124px">
    <div class="service-icon"><svg viewBox="0 0 60 60"><rect x="6" y="12" width="44" height="34" rx="2" fill="none" stroke="var(--icon)" stroke-width="3"/><rect x="12" y="20" width="12" height="14" fill="var(--icon)"/><g stroke="var(--icon)" stroke-width="3"><line x1="28" y1="22" x2="44" y2="22"/><line x1="28" y1="28" x2="44" y2="28"/><line x1="28" y1="34" x2="44" y2="34"/><line x1="12" y1="40" x2="44" y2="40"/></g><path d="M50 18h4v32H12v-4" fill="none" stroke="var(--icon)" stroke-width="3"/></svg></div>
    <h3>Access to Premium<br>Nexora Exchange<br>Account</h3>
  </div>
  <div class="service" style="left:793px;top:124px">
    <div class="service-icon"><svg viewBox="0 0 60 60"><g fill="var(--icon)"><circle cx="16" cy="22" r="5"/><circle cx="44" cy="22" r="5"/><path d="M10 29h12v14h-3v13h-6V43h-3z"/><path d="M38 29h12v14h-3v13h-6V43h-3z"/><rect x="8" y="4" width="14" height="9" rx="1"/><rect x="36" y="4" width="14" height="9" rx="1"/><rect x="24" y="9" width="12" height="8" rx="1"/></g></svg></div>
    <h3>Contract Negotiation<br>&amp; Relationship<br>Management</h3>
  </div>
  <div class="service" style="left:997px;top:124px">
    <div class="service-icon"><svg viewBox="0 0 60 60"><rect x="22" y="8" width="32" height="26" fill="none" stroke="var(--icon)" stroke-width="3"/><path d="M28 28l7-8 5 4 8-9" stroke="var(--icon)" stroke-width="3" fill="none"/><g fill="var(--icon)"><circle cx="14" cy="18" r="6"/><path d="M6 27h14l8 6-2 3-6-3v23h-5V42h-2v14H8z"/></g></svg></div>
    <h3>Ad Server Set-up,<br>training &amp;<br>troubleshooting</h3>
  </div>

  <div class="service" style="left:262px;top:344px">
    <div class="service-icon"><svg viewBox="0 0 60 60"><path d="M6 6h48v48H6zM14 14h14v10H14zM34 14v10h12v8M14 32h10v14M32 32h14v14H32zM24 38h8" fill="none" stroke="#2f5f8f" stroke-width="4"/><path d="M36 38h6" stroke="#5aa0e0" stroke-width="4"/></svg></div>
    <h3>Ad tag<br>implementation &amp;<br>tracking</h3>
  </div>
  <div class="service" style="left:482px;top:344px">
    <div class="service-icon"><svg viewBox="0 0 60 60"><g fill="var(--icon)"><path d="M8 14h22v40H8z" opacity=".55"/><path d="M16 10h22v40H16z" opacity=".75"/><path d="M24 6h20l8 8v38H24z"/></g><path d="M44 6v8h8" fill="#fff"/></svg></div>
    <h3>Propriety Campaign<br>Performance &amp;<br>Reporting Tools</h3>
  </div>
  <div class="service" style="left:694px;top:344px">
    <div class="service-icon"><svg viewBox="0 0 60 60"><rect x="8" y="10" width="34" height="44" rx="2" fill="none" stroke="var(--icon)" stroke-width="3"/><rect x="17" y="6" width="16" height="8" fill="var(--icon)"/><g stroke="var(--icon)" stroke-width="3"><line x1="14" y1="22" x2="36" y2="22"/><line x1="14" y1="30" x2="36" y2="30"/><line x1="14" y1="38" x2="36" y2="38"/><line x1="14" y1="46" x2="28" y2="46"/></g><path d="M48 12h5v34l-2.5 6-2.5-6z" fill="var(--icon)"/></svg></div>
    <h3>Propriety Header<br>Bidder<br>Implementation</h3>
  </div>
  <div class="service" style="left:914px;top:344px">
    <div class="service-icon"><svg viewBox="0 0 60 60"><circle cx="30" cy="30" r="22" fill="none" stroke="var(--icon)" stroke-width="3"/><g stroke="var(--icon)" stroke-width="3"><line x1="30" y1="2" x2="30" y2="10"/><line x1="30" y1="50" x2="30" y2="58"/><line x1="2" y1="30" x2="10" y2="30"/><line x1="50" y1="30" x2="58" y2="30"/></g><g fill="var(--icon)"><circle cx="30" cy="24" r="5"/><circle cx="20" cy="27" r="4"/><circle cx="40" cy="27" r="4"/><path d="M22 40a8 8 0 0 1 16 0z"/><path d="M13 40a7 7 0 0 1 12-3v3zM47 40a7 7 0 0 0-12-3v3z"/></g></svg></div>
    <h3>Audience<br>Segmentation,<br>Targeting &amp; Marketing</h3>
  </div>

  <div class="service" style="left:262px;top:570px">
    <div class="service-icon"><svg viewBox="0 0 60 60"><path d="M12 30a18 18 0 0 1 31-12" stroke="var(--icon)" stroke-width="7" fill="none"/><path d="M48 8v16H32z" fill="var(--icon)"/><path d="M48 30a18 18 0 0 1-31 12" stroke="var(--icon)" stroke-width="7" fill="none"/><path d="M12 52V36h16z" fill="var(--icon)"/></svg></div>
    <h3>Ongoing<br>Optimization</h3>
  </div>
  <div class="service" style="left:482px;top:570px">
    <div class="service-icon"><svg viewBox="0 0 60 60"><rect x="10" y="10" width="34" height="44" rx="2" fill="none" stroke="var(--icon)" stroke-width="3"/><rect x="19" y="6" width="16" height="8" fill="var(--icon)"/><path d="M16 24l3 3 5-6M16 36l3 3 5-6" stroke="var(--icon)" stroke-width="3" fill="none"/><g stroke="var(--icon)" stroke-width="3"><line x1="28" y1="25" x2="38" y2="25"/><line x1="28" y1="37" x2="38" y2="37"/></g><path d="M52 12l4 4-16 18-6 2 2-6z" fill="var(--icon)"/></svg></div>
    <h3>Quality<br>Control</h3>
  </div>
  <div class="service" style="left:694px;top:570px">
    <div class="service-icon"><svg viewBox="0 0 60 60"><g fill="var(--icon)"><circle cx="30" cy="20" r="8"/><circle cx="14" cy="24" r="6"/><circle cx="46" cy="24" r="6"/><path d="M16 46a14 12 0 0 1 28 0z"/><path d="M3 44a11 10 0 0 1 18-7v7zM57 44a11 10 0 0 0-18-7v7z"/></g></svg></div>
    <h3>Direct Advertiser<br>Management</h3>
  </div>
  <div class="service" style="left:914px;top:570px">
    <div class="service-icon"><svg viewBox="0 0 60 60"><g fill="var(--icon)"><path d="M2 20h10l4 20H6z"/><path d="M58 20H48l-4 20h10z"/><path d="M14 22l12-4 10 2 10-2 4 18-6 6-4-4-4 4-4-4-4 4-4-4-3 3-7-5z"/></g><path d="M26 22l-6 8c3 2 6 0 8-3l12 10" stroke="#fff" stroke-width="2" fill="none"/></svg></div>
    <h3>Business<br>Development</h3>
  </div>
</section>

<section class="testimonials">
  <h2 class="section-title">Client Testimonials</h2>
  <div class="rule"></div>
  <div class="avatar" role="img" aria-label="Portrait photo of a smiling client"></div>
  <div class="quote-mark">“</div>
  <p class="quote">Lorem ipsum dolor sit amet, consectetuer adipiscing elit, sed diam nonummy nibh euismod tincidunt ut laoreet dolore magna aliquam erat volutpat. Ut wisi enim ad minim veniam, quis nostrud exerci tation ullamcorper suscipit lobortis nisl ut aliquip commodo consequat. Duis autem vel eum iriure dolor in hendrerit in vulputate velit esse molestie consequat, vel illum dolore eu feugiat nulla facilisis at vero eros et accumsan et iusto odio dignissimaugue duis dolore te feugait nulla facilisi.</p>
  <div class="quote-author">.... Maren Oldfield, Tallquist Media , USA</div>
  <a class="more-link">Read more testimonials »</a>
</section>

<footer class="site-footer">
  <div class="footer-col quick-links">
    <h4>Quick Links</h4>
    <ul><li>Home</li><li>About Us</li><li>Publisher</li><li>Advertiser</li><li>Contact Us</li></ul>
  </div>
  <div class="col-divider" style="left:204px"></div>
  <div class="footer-col contact-details">
    <h4>Contact Details</h4>
    <address>Zornival<br>48, Larkfield Row, Ostrave,<br>Belmire, Tarnholt - 604 219</address>
    <div class="line"><svg width="13" height="13" viewBox="0 0 24 24"><path fill="#fff" d="M6.6 10.8a15 15 0 0 0 6.6 6.6l2.2-2.2c.3-.3.7-.4 1-.2 1.1.4 2.3.6 3.6.6.6 0 1 .4 1 1V20c0 .6-.4 1-1 1A17 17 0 0 1 3 4c0-.6.4-1 1-1h3.5c.6 0 1 .4 1 1 0 1.3.2 2.5.6 3.6.1.3 0 .7-.2 1z"/></svg>555-014-2768</div>
    <div class="line"><svg width="14" height="13" viewBox="0 0 24 22"><path fill="#fff" d="M6 0h12v6H6zM0 7h24v10h-5v5H5v-5H0z"/><path fill="#2b2b2b" d="M7 14h10v6H7z"/></svg>555-014-2769</div>
    <div class="line"><svg width="13" height="10" viewBox="0 0 24 18"><path fill="#fff" d="M0 0h24v18H0z"/><path d="M0 0l12 9L24 0" stroke="#2b2b2b" stroke-width="2" fill="none"/></svg>info@zornival.com</div>
  </div>
  <div class="col-divider" style="left:500px"></div>
  <div class="footer-col inquiry">
    <h4>Quick Inquiry</h4>
    <div class="field" style="top:72px;height:35px;line-height:23px">Name</div>
    <div class="field" style="top:114px;height:35px;line-height:23px">Phone</div>
    <div class="field" style="top:155px;height:57px">Message</div>
    <div class="btn-submit">Submit</div>
  </div>
  <div class="col-divider" style="left:898px"></div>
  <div class="footer-mark"></div>
</footer>

<div class="copyright">Copyright © 2016 Zornival. All Rights Reserved.</div>

</body>
</html>
```